Trulock Property Inspections

Property Inspection ( pre-purchase building inspections, swimming pool inspection, pest inspection , maintenance)

Industry/Entity Type

Building

Contact Information for Business Card

Omar Tanvelli
info@trulockinspections.com.au
0417 828 691

TruLock Property Inspections
www.trulockinspections.com.au

on the back

Property Inspections
Property Maintenance

Safe Home....Safe Familu

```html
<!DOCTYPE html>
<html lang="en">
<head>
<meta charset="utf-8">
<title>Trulock Property Inspections – Business Card</title>
<link href="https://fonts.googleapis.com/css2?family=Open+Sans:wght@400;600;700&display=swap" rel="stylesheet">
<style>
  :root {
    --backdrop: #e9e6e1;
    --card-white: #ffffff;
    --ink: #1c1c1e;
    --ink-soft: #4a4a4e;
    --brand-blue: #3d7fd6;
    --brand-blue-deep: #1f5fb8;
    --night: #0b0b0d;
    --night-lift: #2a2b2f;
    --divider: #9a9a9e;
  }
  * { box-sizing: border-box; margin: 0; padding: 0; }
  html, body {
    width: 1200px; height: 800px; overflow: hidden;
    background: var(--backdrop);
    font-family: "Open Sans", Arial, sans-serif;
  }
  .canvas {
    position: relative; width: 1200px; height: 800px;
    display: flex; align-items: center; justify-content: center; gap: 60px;
  }
  .card {
    position: relative; width: 520px; height: 297px;
    border-radius: 18px; overflow: hidden;
    box-shadow: 0 10px 26px rgba(0,0,0,0.22);
  }

  /* Back side */
  .card--back {
    background: linear-gradient(150deg, var(--night-lift) 0%, var(--night) 55%, var(--night) 100%);
  }
  .back-brand {
    position: absolute; left: 48px; top: 92px; width: 380px;
  }
  .back-brand__name {
    color: var(--brand-blue); font-weight: 600; font-size: 30px; line-height: 1.15;
  }
  .back-brand__tagline {
    margin-top: 10px; color: var(--brand-blue); font-size: 15px; letter-spacing: 0.3px;
  }
  .back-band {
    position: absolute; left: 0; right: 0; bottom: 0; height: 46px;
    background: linear-gradient(90deg, var(--brand-blue-deep), var(--brand-blue));
    display: flex; align-items: center; justify-content: flex-end; padding-right: 28px;
  }
  .back-band__services {
    color: var(--ink); font-size: 14px;
  }

  /* Front side */
  .card--front { background: var(--card-white); }
  .front-brand {
    position: absolute; left: 30px; top: 88px; width: 210px;
  }
  .front-brand__name {
    color: var(--ink); font-weight: 600; font-size: 22px; line-height: 1.2;
  }
  .front-brand__tagline {
    margin-top: 14px; color: var(--ink); font-size: 14px;
  }
  .front-divider {
    position: absolute; left: 262px; top: 56px; width: 1px; height: 120px;
    background: var(--divider);
  }
  .contact {
    position: absolute; left: 286px; top: 60px;
  }
  .contact__name {
    color: var(--brand-blue); font-weight: 700; font-size: 16px; letter-spacing: 0.5px;
    text-transform: uppercase; margin-bottom: 12px;
  }
  .contact__list { list-style: none; }
  .contact__item {
    display: flex; align-items: center; gap: 8px;
    font-size: 11.5px; color: var(--ink-soft); line-height: 1.9;
  }
  .contact__icon { width: 12px; height: 12px; flex: none; }
  .front-swoosh { position: absolute; left: 0; bottom: 0; width: 520px; height: 120px; }
  .front-website {
    position: absolute; right: 36px; bottom: 20px;
    color: var(--card-white); font-size: 13px; font-weight: 600; letter-spacing: 1px;
  }
</style>
</head>
<body>
<main class="canvas">

  <section class="card card--back" aria-label="Card back">
    <div class="back-brand">
      <p class="back-brand__name">Trulock Property Inspections</p>
      <p class="back-brand__tagline">Sure Checks...Sound Living</p>
    </div>
    <div class="back-band">
      <p class="back-band__services">Property Inspection | Property Maintenance</p>
    </div>
  </section>

  <section class="card card--front" aria-label="Card front">
    <div class="front-brand">
      <p class="front-brand__name">Trulock Property Inspections</p>
      <p class="front-brand__tagline">Sure Checks...Sound Living</p>
    </div>

    <div class="front-divider"></div>

    <div class="contact">
      <p class="contact__name">Omar Tanvelli</p>
      <ul class="contact__list">
        <li class="contact__item">
          <svg class="contact__icon" viewBox="0 0 12 12" aria-hidden="true">
            <rect width="12" height="12" rx="2" fill="var(--brand-blue)"/>
            <path d="M3.5 2.8c.4-.3.9-.2 1.1.2l.6 1.1c.2.4.1.7-.2 1l-.4.3c.4.9 1 1.5 1.9 1.9l.3-.4c.3-.3.6-.4 1-.2l1.1.6c.4.2.5.7.2 1.1l-.5.6c-.4.4-1 .5-1.6.3C5.1 8.6 3.4 6.9 2.7 5c-.2-.6-.1-1.2.3-1.6z" fill="#fff"/>
          </svg>
          (02) 9385 2617
        </li>
        <li class="contact__item">
          <svg class="contact__icon" viewBox="0 0 12 12" aria-hidden="true">
            <rect width="12" height="12" rx="2" fill="var(--brand-blue)"/>
            <rect x="4" y="2.2" width="4" height="7.6" rx="0.8" fill="none" stroke="#fff" stroke-width="1"/>
            <circle cx="6" cy="8.4" r="0.5" fill="#fff"/>
          </svg>
          0417 828 691
        </li>
        <li class="contact__item">
          <svg class="contact__icon" viewBox="0 0 12 12" aria-hidden="true">
            <rect width="12" height="12" rx="2" fill="var(--brand-blue)"/>
            <rect x="2.3" y="3.5" width="7.4" height="5" rx="0.6" fill="#fff"/>
            <path d="M2.6 3.8 6 6.4l3.4-2.6" fill="none" stroke="var(--brand-blue)" stroke-width="0.8"/>
          </svg>
          info@trulockinspections.com.au
        </li>
      </ul>
    </div>

    <svg class="front-swoosh" viewBox="0 0 520 120" preserveAspectRatio="none" aria-hidden="true">
      <path d="M0 120 L0 112 C120 96 300 86 520 40 L520 120 Z" fill="var(--night)"/>
      <path d="M0 112 C120 96 300 86 520 40 L520 46 C300 92 120 102 0 118 Z" fill="var(--night-lift)"/>
    </svg>
    <p class="front-website">www.trulockinspections.com.au</p>
  </section>

</main>
</body>
</html>
```